Dental Savings Plan - Marcus Delvane DDS

We need a tri-fold brochure and 1 page flyer/poster for Dr. Marcus Delvane' dental office located on Maui, Hawaii. We are offering a new "Dental Savings Plan" to patients.
I have included 3 photos, along with the office logo. You do not have to use all photos if you do not want to. We want this to catch the eyes of patients, easy for them to read and understand, and to show them that this is a much better option than dental insurance.
Please use same Hawaiian theme and colors on the office website https://www.pearlreefcare.com .

Please also include the following to promote this new plan:

Dental Services Include
• Professional Dental Cleanings (2 per benefit year)
• Perio Maintenance Cleanings (3 per benefit year) covered at 80%
• Radiographs as needed (1 set of X-rays per benefit year)
• Doctor Examinations (2 per benefit year)
• Ozone Treatment
• KOROV Amalgam Removal
• Additional limited/emergency exam (1 per benefit year)
• Cosmetic consultation
• 15% discount on all other services (including cosmetic procedures)
• 10% discount on implants and implant crowns

Advantages of the Dental Savings Plan
1. No deductibles
2. No waiting periods
3. No claims to file
4. No frequency limitations or exclusions
5. No yearly maximum benefits
6. No pre-authorization requirements
7. No pre-existing conditions limitations
8. State of the art facility and technology
9. Immediate enrollment
10. Highest quality of care for you and your Ohana

Annual Fee
$399 first family member/individual (equivalent to $33 per month)
$349 second family member (equivalent to $29 per month)
$249 each additional family member (equivalent to $20 per month)

Provisions of the Dental Savings Plan
• May not be combined with insurance plans, discounts or promotions
• This Dental Savings Plan is not an insurance plan, but a payment arrangement provided by Marcus Delvane DDS, and is not transferable to any other dental office or dental specialist
• Payment for services are due at the date of service
• This program is for you and is not transferable
• Benefits are provided for one year from the date the plan is purchased
• Must be paid in full when starting the plan
• No refunds will be provided for dues of the plan annual fee under any circumstances, including failure to schedule and maintain appointments
• If Paxwel Fund is used to pay for the program and for services then only a 10% discount will be given
• To receive the full 15% discount on restorative treatment, you must schedule the appointment the day it is recommended. Any failed appointment results in the loss of the 15% discount.

Target Market(s)

Dental patients without dental insurance

Industry/Entity Type

Dental Clinic

Requirements
Must have
• My project must have the logo file to identify the dental office, Hawaiian theme, same colors as website, match style of website font, theme and colors, as well as, all the Dental Services, Advantages of the Dental Savings Plan, Annual Fee, and the Provisions of the Dental Savings Plan.

```html
<!DOCTYPE html>
<html lang="en">
<head>
<meta charset="utf-8">
<title>Dental Savings Plan – Marcus Delvane DDS</title>
<link href="https://fonts.googleapis.com/css2?family=Open+Sans:wght@400;600;700;800&family=Cinzel:wght@400;600&display=swap" rel="stylesheet">
<style>
:root{
  --blue:#1b8fd2;
  --blue-dark:#0d6aad;
  --blue-deep:#0a4f86;
  --blue-light:#e8f4fc;
  --green:#7dc243;
  --green-dark:#5ea22b;
  --ink:#3b4a55;
  --paper:#ffffff;
  --bg:#e9ecef;
}
*{box-sizing:border-box;margin:0;padding:0}
html,body{width:880px;height:1200px;overflow:hidden}
body{background:var(--bg);font-family:"Open Sans",Arial,sans-serif;color:var(--ink);position:relative}
.sheet{position:absolute;left:20px;width:840px;display:flex;box-shadow:0 6px 18px rgba(0,0,0,.22);background:var(--paper)}
.sheet--outside{top:30px;height:540px}
.sheet--inside{top:610px;height:560px}
.panel{position:relative;width:280px;height:100%;overflow:hidden}
.panel + .panel{border-left:1px solid rgba(0,0,0,.08)}
.photo{position:absolute;left:0;right:0;top:0}
.wave{position:absolute;left:0;width:280px;display:block}
.bar{position:absolute;left:0;right:0;bottom:0;height:38px;display:flex;align-items:center;justify-content:center;gap:8px;color:#fff;font-weight:700;font-size:12px;letter-spacing:.5px}
.bar--blue{background:var(--blue-dark)}
.bar--green{background:var(--green)}
.bar svg{width:14px;height:14px}

/* outside left */
.intro{position:absolute;top:248px;left:24px;right:24px}
.intro__title{background:var(--green);color:#fff;font-weight:700;font-size:15px;padding:6px 12px;margin-left:-24px;width:215px;border-radius:0 20px 20px 0}
.intro p{font-size:10px;line-height:1.55;margin-top:12px}

/* outside middle */
.panel--contact{background:linear-gradient(180deg,var(--blue) 0%,var(--blue-dark) 100%);color:#fff;text-align:center}
.map{position:absolute;top:18px;left:24px;width:232px;height:110px;border:3px solid #fff;background:linear-gradient(135deg,#cfe6c3,#e9efe4 60%,#bcd9ee)}
.contact{position:absolute;top:140px;left:20px;right:20px}
.heading-white{font-weight:800;font-size:15px;letter-spacing:1px}
.contact p{font-size:10.5px;line-height:1.6;margin-top:4px}
.logo{display:flex;align-items:center;justify-content:center;gap:8px;font-weight:700}
.logo__dot{width:14px;height:14px;border-radius:50%;background:var(--green)}
.logo--white{color:#fff;font-size:16px;margin-top:24px}
.hours{position:absolute;top:300px;left:30px;right:30px}
.hours dl{display:grid;grid-template-columns:1fr 1fr;font-size:10.5px;line-height:1.75;margin-top:8px;text-align:left}
.hours dd{text-align:right}

/* outside right */
.logo--cover{position:absolute;top:38px;left:0;right:0;color:var(--blue-dark);font-size:20px}
.cover-photo{position:absolute;top:96px;left:0;right:0;height:260px}
.cover-title{position:absolute;top:380px;left:0;right:0;text-align:center;font-family:"Cinzel",Georgia,serif;color:var(--blue-dark);font-size:27px;line-height:1.2;font-weight:600}

/* inside */
.section-head{display:flex;align-items:center;gap:10px}
.section-head svg{flex:none;width:34px;height:34px}
.section-head h2{font-size:13px;font-weight:800;line-height:1.25;letter-spacing:.3px}
.services{position:absolute;top:200px;left:20px;right:18px}
.services .section-head h2{color:var(--blue-dark)}
.ticks{list-style:none;margin-top:10px}
.ticks li{position:relative;padding-left:14px;font-size:9.3px;line-height:1.4;margin-bottom:3px}
.ticks li::before{content:"";position:absolute;left:0;top:4px;width:6px;height:6px;border-radius:50%;background:var(--green)}
.discounts{position:absolute;left:20px;right:20px;bottom:50px;display:flex;gap:10px}
.discount{flex:1;background:var(--blue);color:#fff;border-radius:6px;padding:8px;font-size:9px;line-height:1.35}
.discount b{display:block;font-size:15px}
.discount--green{background:var(--green)}

.panel--fees{background:linear-gradient(180deg,var(--blue) 0%,var(--blue-dark) 100%);color:#fff}
.fees{position:absolute;top:22px;left:22px;right:22px}
.fees .heading-white{font-size:18px;text-align:center}
.fees ul{list-style:none;margin-top:12px}
.fees li{font-size:10px;line-height:1.45;margin-bottom:9px;padding-left:14px;position:relative}
.fees li::before{content:"";position:absolute;left:0;top:4px;width:7px;height:7px;background:var(--green);border-radius:50%}
.fees li b{font-size:12px}
.advantages{position:absolute;top:210px;left:16px;right:16px;bottom:50px;background:#fff;border-radius:8px;padding:14px 14px 10px;color:var(--ink)}
.advantages .section-head h2{color:var(--blue-dark)}
.advantages ol{margin-top:10px;padding-left:18px}
.advantages li{font-size:9.6px;line-height:1.4;margin-bottom:4px}
.advantages li::marker{color:var(--green-dark);font-weight:700}

.panel--provisions{background:var(--blue-light)}
.provisions{position:absolute;top:184px;left:18px;right:16px}
.provisions .section-head h2{color:var(--blue-dark)}
.provisions .ticks li{font-size:8.7px;line-height:1.36;margin-bottom:3px}
</style>
</head>
<body>

<!-- Outside spread -->
<section class="sheet sheet--outside">
  <article class="panel panel--doctor">
    <div class="photo" style="height:230px;background:linear-gradient(160deg,#9fd3f0 0%,#e6d3b8 70%,#d9bfa0 100%)" role="img" aria-label="Smiling couple embracing on a sunny beach"></div>
    <svg class="wave" style="top:196px" viewBox="0 0 280 44" height="44" aria-hidden="true">
      <path d="M0 18 Q140 48 280 6 L280 44 L0 44Z" fill="var(--green)"/>
      <path d="M0 28 Q140 54 280 16 L280 44 L0 44Z" fill="#fff"/>
    </svg>
    <div class="intro">
      <div class="intro__title">Dr. Marcus Delvane</div>
      <p>Welcome to Pearl Reef Care. Our gentle team on Maui cares for your whole family with modern dentistry, honest advice and a warm island welcome.</p>
      <p>The Dental Savings Plan gives patients without insurance a simple yearly fee, routine care included and savings on every other treatment we offer.</p>
      <p>Dr. Marcus Delvane' practice looks forward to welcoming you and your Ohana.</p>
    </div>
    <div class="bar bar--blue">RESERVE AN APPOINTMENT</div>
  </article>

  <article class="panel panel--contact">
    <div class="map" role="img" aria-label="Street map showing the office location in Kihei"></div>
    <div class="contact">
      <div class="heading-white">CONTACT US</div>
      <p>(808) 555-0142<br>410 Lanikai Way, Kihei, HI 96753<br>info@pearlreefcare.com</p>
      <div class="logo logo--white"><span class="logo__dot"></span>Pearl Reef Care</div>
    </div>
    <div class="hours">
      <div class="heading-white">OUR HOURS</div>
      <dl>
        <dt>Monday</dt><dd>8:00 – 5:00</dd>
        <dt>Tuesday</dt><dd>8:00 – 5:00</dd>
        <dt>Wednesday</dt><dd>8:00 – 5:00</dd>
        <dt>Thursday</dt><dd>8:00 – 5:00</dd>
        <dt>Friday</dt><dd>8:00 – 2:00</dd>
        <dt>Sat – Sun</dt><dd>Closed</dd>
      </dl>
    </div>
    <div class="bar bar--green">
      <svg viewBox="0 0 24 24" fill="#fff" aria-hidden="true"><path d="M6.6 10.8a15 15 0 006.6 6.6l2.2-2.2a1 1 0 011-.25 11.4 11.4 0 003.6.6 1 1 0 011 1V20a1 1 0 01-1 1A17 17 0 013 4a1 1 0 011-1h3.5a1 1 0 011 1 11.4 11.4 0 00.6 3.6 1 1 0 01-.25 1z"/></svg>
      (808) 555-0142
    </div>
  </article>

  <article class="panel panel--cover">
    <div class="logo logo--cover"><span class="logo__dot"></span>Pearl Reef Care</div>
    <div class="cover-photo" style="background:linear-gradient(180deg,#cfe3ee 0%,#e9d7c7 60%,#c9a58a 100%)" role="img" aria-label="Smiling young woman with a bright healthy smile"></div>
    <svg class="wave" style="top:332px" viewBox="0 0 280 30" height="30" aria-hidden="true">
      <path d="M0 30 Q140 0 280 22 L280 30Z" fill="#fff"/>
    </svg>
    <h1 class="cover-title">DENTAL<br>SAVINGS PLAN</h1>
    <div class="bar bar--blue">https://www.pearlreefcare.com</div>
  </article>
</section>

<!-- Inside spread -->
<section class="sheet sheet--inside">
  <article class="panel panel--services">
    <div class="photo" style="height:185px;background:linear-gradient(150deg,#bfe0f2 0%,#e4eef4 50%,#d6c2b2 100%)" role="img" aria-label="Dentist examining a patient's teeth in the dental chair"></div>
    <svg class="wave" style="top:160px" viewBox="0 0 280 34" height="34" aria-hidden="true">
      <path d="M0 10 Q140 40 280 8 L280 34 L0 34Z" fill="var(--blue)"/>
      <path d="M0 20 Q140 46 280 18 L280 34 L0 34Z" fill="#fff"/>
    </svg>
    <div class="services">
      <div class="section-head">
        <svg viewBox="0 0 34 34" aria-hidden="true"><circle cx="17" cy="17" r="17" fill="var(--blue)"/><path d="M11 10c2-1.5 4 0 6 0s4-1.5 6 0c2 2 1 6 0 8-1 3-1 7-2.5 7S19 20 17 20s-2 5-3.5 5S12 21 11 18c-1-2-2-6 0-8z" fill="#fff"/></svg>
        <h2>DENTAL SERVICES<br>INCLUDE</h2>
      </div>
      <ul class="ticks">
        <li>Professional Dental Cleanings (2 per benefit year)</li>
        <li>Perio Maintenance Cleanings (3 per benefit year) covered at 80%</li>
        <li>Radiographs as needed (1 set of X-rays per benefit year)</li>
        <li>Doctor Examinations (2 per benefit year)</li>
        <li>Ozone Treatment</li>
        <li>KOROV Amalgam Removal</li>
        <li>Additional limited/emergency exam (1 per benefit year)</li>
        <li>Cosmetic consultation</li>
      </ul>
    </div>
    <div class="discounts">
      <div class="discount"><b>15% discount</b>on all other services (including cosmetic procedures)</div>
      <div class="discount discount--green"><b>10% discount</b>on implants and implant crowns</div>
    </div>
    <div class="bar bar--green">https://www.pearlreefcare.com</div>
  </article>

  <article class="panel panel--fees">
    <div class="fees">
      <div class="heading-white">ANNUAL FEE</div>
      <ul>
        <li><b>$399</b> first family member/individual (equivalent to $33 per month)</li>
        <li><b>$349</b> second family member (equivalent to $29 per month)</li>
        <li><b>$249</b> each additional family member (equivalent to $20 per month)</li>
      </ul>
    </div>
    <div class="advantages">
      <div class="section-head">
        <svg viewBox="0 0 34 34" aria-hidden="true"><circle cx="17" cy="17" r="17" fill="var(--green)"/><path d="M10 17l5 5 9-10" stroke="#fff" stroke-width="3" fill="none" stroke-linecap="round" stroke-linejoin="round"/></svg>
        <h2>ADVANTAGES OF THE<br>DENTAL SAVINGS PLAN</h2>
      </div>
      <ol>
        <li>No deductibles</li>
        <li>No waiting periods</li>
        <li>No claims to file</li>
        <li>No frequency limitations or exclusions</li>
        <li>No yearly maximum benefits</li>
        <li>No pre-authorization requirements</li>
        <li>No pre-existing conditions limitations</li>
        <li>State of the art facility and technology</li>
        <li>Immediate enrollment</li>
        <li>Highest quality of care for you and your Ohana</li>
      </ol>
    </div>
    <div class="bar bar--green">
      <svg viewBox="0 0 24 24" fill="#fff" aria-hidden="true"><path d="M6.6 10.8a15 15 0 006.6 6.6l2.2-2.2a1 1 0 011-.25 11.4 11.4 0 003.6.6 1 1 0 011 1V20a1 1 0 01-1 1A17 17 0 013 4a1 1 0 011-1h3.5a1 1 0 011 1 11.4 11.4 0 00.6 3.6 1 1 0 01-.25 1z"/></svg>
      (808) 555-0142
    </div>
  </article>

  <article class="panel panel--provisions">
    <div class="photo" style="height:170px;background:linear-gradient(160deg,#a9d6f0 0%,#dfe9d8 55%,#d8bca2 100%)" role="img" aria-label="Happy family of four smiling together outdoors"></div>
    <svg class="wave" style="top:146px" viewBox="0 0 280 30" height="30" aria-hidden="true">
      <path d="M0 8 Q140 38 280 6 L280 30 L0 30Z" fill="var(--green)"/>
      <path d="M0 16 Q140 44 280 14 L280 30 L0 30Z" fill="var(--blue-light)"/>
    </svg>
    <div class="provisions">
      <div class="section-head">
        <svg viewBox="0 0 34 34" aria-hidden="true"><circle cx="17" cy="17" r="17" fill="var(--blue)"/><rect x="11" y="9" width="12" height="16" rx="1.5" fill="#fff"/><path d="M14 14h6M14 17h6M14 20h4" stroke="var(--blue)" stroke-width="1.5"/></svg>
        <h2>PROVISIONS OF THE<br>DENTAL SAVINGS PLAN</h2>
      </div>
      <ul class="ticks">
        <li>May not be combined with insurance plans, discounts or promotions</li>
        <li>This Dental Savings Plan is not an insurance plan, but a payment arrangement provided by Marcus Delvane DDS, and is not transferable to any other dental office or dental specialist</li>
        <li>Payment for services are due at the date of service</li>
        <li>This program is for you and is not transferable</li>
        <li>Benefits are provided for one year from the date the plan is purchased</li>
        <li>Must be paid in full when starting the plan</li>
        <li>No refunds will be provided for dues of the plan annual fee under any circumstances, including failure to schedule and maintain appointments</li>
        <li>If Paxwel Fund is used to pay for the program and for services then only a 10% discount will be given</li>
        <li>To receive the full 15% discount on restorative treatment, you must schedule the appointment the day it is recommended. Any failed appointment results in the loss of the 15% discount.</li>
      </ul>
    </div>
    <div class="bar bar--blue">https://www.pearlreefcare.com</div>
  </article>
</section>

</body>
</html>
```